Business Card Re-Design/Update

We'd like to update out business cards. I've included our current "Style guide" which has the colour scheme of the organisation in it. I've also included the branding files with logos etc in them.

I've also included a copy of one of our existing cards so that you can see how ugly/dated they look. I'd like a fresh modern corporate look.

Target Market(s)

These are for our clients, potential clients, industry contacts - like all business cards

Contact Information for Business Card

Name
Position
Company Address - Level 1, 47 Garnet Lane, Toowong Qld 4066
Direct Phone
mobile
Email
Website -www.korvalnet.com.au
Logo

Colors

Designer to choose colors to be used in the design.

Requirements
Must have
• Main Logo
• Cards will need to be editable to be able to personalize them for each new employee.
Nice to have
• The MapOUT, HandOVER, UpKEEP would be okay to have if they can be sensibly and professionally added to the look without detracting from the main imagery.
• Maybe they could go on the back of the card? will leave this to your creative discretion as to whether/where they fit.
Should not have
• Should not have decorative or script fonts

```html
<!DOCTYPE html>
<html lang="en">
<head>
<meta charset="utf-8">
<title>korvalnet business card</title>
<link rel="stylesheet" href="https://fonts.googleapis.com/css2?family=Arimo:wght@400;700&display=swap">
<style>
  :root {
    --backdrop: #e4e4e4;
    --card-white: #f7f7f7;
    --brand-red: #b21c22;
    --red-light: #d01a21;
    --red-dark: #a30f14;
    --ink: #1e1e1e;
    --ink-soft: #4a4a4a;
    --white: #ffffff;
  }
  * { margin: 0; padding: 0; box-sizing: border-box; }
  html, body { width: 1200px; height: 960px; overflow: hidden; }
  body {
    background: var(--backdrop);
    font-family: "Arimo", Arial, sans-serif;
    position: relative;
  }
  .card {
    position: absolute;
    width: 600px;
    height: 343px;
    overflow: hidden;
  }
  .card-front { left: 314px; top: 113px; background: var(--card-white); }
  .card-back {
    left: 311px; top: 472px;
    background: linear-gradient(180deg, var(--red-light) 0%, var(--red-dark) 100%);
  }
  .holder-name {
    position: absolute; left: 45px; top: 53px;
    font-size: 20px; font-weight: 700; color: var(--brand-red);
    letter-spacing: 0.2px;
  }
  .holder-role {
    position: absolute; left: 45px; top: 77px;
    font-size: 14px; color: var(--ink);
  }
  .wordmark {
    position: absolute; left: 324px; top: 58px;
    display: flex; align-items: center; gap: 12px;
  }
  .wordmark-square { width: 26px; height: 26px; background: var(--brand-red); }
  .wordmark-name { font-size: 29px; font-weight: 700; color: var(--ink); letter-spacing: -0.3px; }
  .address {
    position: absolute; left: 46px; top: 146px;
    font-size: 14px; line-height: 18px; color: var(--ink-soft);
  }
  .contact-list {
    position: absolute; left: 48px; top: 191px;
    list-style: none; font-size: 14px; color: var(--ink-soft);
  }
  .contact-list li { display: flex; align-items: center; height: 19px; gap: 8px; }
  .contact-list svg { width: 13px; height: 13px; fill: var(--brand-red); flex: none; }
  .web-band {
    position: absolute; left: 0; bottom: 0; width: 100%; height: 24px;
    background: linear-gradient(180deg, var(--red-light), var(--red-dark));
  }
  .web-address {
    position: absolute; left: 46px; top: 4px;
    font-size: 13px; color: var(--white); letter-spacing: 2.4px;
  }
  .band-accent { position: absolute; left: 428px; top: 296px; }
  .back-name {
    position: absolute; left: 0; width: 100%; top: 132px;
    text-align: center; font-size: 46px; font-weight: 700; color: var(--white);
    letter-spacing: -0.5px;
  }
  .service-row {
    position: absolute; top: 278px; left: 46px;
    display: flex; gap: 34px;
  }
  .service { display: flex; align-items: center; gap: 9px; }
  .service-square { width: 22px; height: 22px; background: var(--white); }
  .service-name { font-size: 25px; font-weight: 700; color: var(--white); }
</style>
</head>
<body>
  <section class="card card-front">
    <h1 class="holder-name">MAREN HALE</h1>
    <p class="holder-role">Business Development Manager</p>

    <div class="wordmark">
      <span class="wordmark-square"></span>
      <span class="wordmark-name">korvalnet</span>
    </div>

    <address class="address" style="font-style:normal">
      Level 1, 47 Garnet Lane<br>Toowong QLD 4066
    </address>

    <ul class="contact-list">
      <li><svg viewBox="0 0 16 16"><path d="M3 1l3 3-1.5 2a9 9 0 0 0 5.5 5.5L12 10l3 3-2 2C6 15 1 10 1 3z"/></svg>+61 (0)7 3180 4410</li>
      <li><svg viewBox="0 0 16 16"><path d="M3 1l3 3-1.5 2a9 9 0 0 0 5.5 5.5L12 10l3 3-2 2C6 15 1 10 1 3z"/></svg>+61 (0)7 3180 4416</li>
      <li><svg viewBox="0 0 16 16"><path d="M4 0h8v16H4zM5.5 2v10h5V2zM7 13.5h2v1H7z" fill-rule="evenodd"/></svg>+61 (0)412 555 093</li>
      <li><svg viewBox="0 0 16 16"><path d="M4 1h8v4H4zM1 6h14v7h-2v2H3v-2H1zM4 10v4h8v-4z" fill-rule="evenodd"/></svg>+61 (0)7 3180 4403</li>
      <li><svg viewBox="0 0 16 16"><path d="M1 3h14v10H1zM2 4.5v.5l6 4 6-4v-.5z" fill-rule="evenodd"/></svg>mhale@korvalnet.com.au</li>
    </ul>

    <svg class="band-accent" width="40" height="47" viewBox="0 0 40 47">
      <polygon points="0,0 5,0 25,23 20,23" fill="var(--brand-red)"/>
      <polygon points="20,23 25,23 36,47 31,47" fill="var(--white)"/>
    </svg>
    <div class="web-band">
      <span class="web-address">www.korvalnet.com.au</span>
    </div>
  </section>

  <section class="card card-back">
    <p class="back-name">korvalnet</p>
    <div class="service-row">
      <div class="service"><span class="service-square"></span><span class="service-name">MapOUT</span></div>
      <div class="service"><span class="service-square"></span><span class="service-name">HandOVER</span></div>
      <div class="service"><span class="service-square"></span><span class="service-name">UpKEEP</span></div>
    </div>
  </section>
</body>
</html>
```